Logo/ business card idea for a weld inspection/ nondestructive testing LLC

I have just started an LLC (my first) for weld inspection and non-destructive testing. I am the president and only member of this company. It is a very niche industry and word of mouth is basically the only advertisement needed to get you the next job. I will offer magnetic particle, dye penetrant, ultrasonic, and visual testing for the non-destructive services. X-ray is a form of non-destructive testing that I spent a few years doing but to costly for me at this time. All pipelines under the ground are welded, visually inspected and x-ray by someone just like me. All new building construction, any type of nuclear plant , pressure vessel, ect. , the welds are inspected by someone like me. Its is every increasing also with safety concerns. People are living right next to this stuff!!I will be the guy that fabrication shops or construction companies call to give the final OK that the welds are satisfactory after inspection to a certain code or standard. The designers have all the freedom they wish but I have attached a PDF with greater explanations and color ideas. I want raised glossy print on the front of the card and the necessary info. The back will not have raised print and serve more as a brief resume listing the certifications I have. The company only cares about the certifications and ultimately my signature. I want to make the front of the car into a fridge magnet to pass out with the card also. Something that is appealing to hang up instead of getting lost in someones wallet. The final design………. should be classic and stand the test of time. It should communicate precision and accuracy as well as incorporate the sound beam you will find in the PDF I’ve attached.Thanks and have a great day,Dale

Target Market(s)

Adult males in english speaking countries that handle welding and/or construction duties. Most of the time under heavy time constraints and deadlines. Ages 30-60

Industry/Entity Type

Construction

Contact Information for Business Card

Halvern Inspection Services, LLC
Dale Halvern
Ithaca, MI
989-514-2730
halv7dw@mailbreeze.net

Font styles to use
Other font styles liked:
• designers choice

Requirements
Nice to have
• The logo on the front can completely encase the Halvern, be segmented incorporating the Halvern, or next to it. There can also be a couple of “flaws” (the red, blue and yellow in some of the pictures attached in the PDF) in the sound beam spread.

```html
<!DOCTYPE html>
<html lang="en">
<head>
<meta charset="utf-8">
<title>Halvern Inspection Services, LLC — Business Card</title>
<link rel="stylesheet" href="https://fonts.googleapis.com/css2?family=Archivo+Narrow:wght@400;500;700&display=swap">
<style>
  :root {
    --bg: #a9a9a9;
    --card: #ececec;
    --card-edge: #e2e2e2;
    --brand-blue: #2f66a3;
    --band-blue: #4279b7;
    --band-blue-light: #5088c4;
    --text-white: #ffffff;
    --shadow: rgba(0, 0, 0, 0.28);
  }
  * { box-sizing: border-box; margin: 0; padding: 0; }
  html, body {
    width: 1200px; height: 1000px; overflow: hidden;
    background: var(--bg);
    font-family: "Archivo Narrow", "Arial Narrow", sans-serif;
  }
  .stage { position: relative; width: 1200px; height: 1000px; }

  .card {
    position: absolute;
    width: 680px; height: 390px;
    background: linear-gradient(160deg, #f2f2f2 0%, var(--card) 60%, var(--card-edge) 100%);
    box-shadow: 0 6px 14px var(--shadow);
    overflow: hidden;
  }

  /* Front */
  .card--front { left: 90px; top: 100px; }
  .company {
    position: absolute; left: 62px; top: 150px;
    display: flex; align-items: center; gap: 16px;
  }
  .company__square {
    width: 18px; height: 18px;
    background: var(--brand-blue);
    flex: none;
  }
  .company__name {
    color: var(--brand-blue);
    font-size: 42px;
    font-weight: 500;
    line-height: 1;
    white-space: nowrap;
  }
  .contact-band {
    position: absolute; left: 0; right: 0; bottom: 0; height: 110px;
    background: linear-gradient(90deg, var(--brand-blue) 0%, var(--band-blue) 55%, var(--band-blue-light) 100%);
    display: flex; align-items: center;
    padding: 20px 0 0 62px;
    color: var(--text-white);
    font-size: 23px;
  }
  .contact-band__name { font-weight: 700; letter-spacing: 0.5px; }
  .contact-band__sep { margin: 0 14px; opacity: 0.9; }

  /* Back */
  .card--back { left: 430px; top: 510px; }
  .credentials {
    position: absolute; left: 12px; top: 58px;
    width: 505px; height: 222px;
    background: linear-gradient(135deg, var(--band-blue-light) 0%, var(--band-blue) 50%, var(--brand-blue) 100%);
    color: var(--text-white);
    font-size: 23px; line-height: 1.2;
    letter-spacing: 0.4px;
    padding: 26px 0 0 62px;
  }
  .credentials__group { list-style: none; }
  .credentials__group + .credentials__group { margin-top: 8px; margin-left: -8px; }
  .credentials__method { padding-left: 92px; }
</style>
</head>
<body>
<main class="stage">
  <section class="card card--front" aria-label="Business card front">
    <div class="company">
      <span class="company__square" aria-hidden="true"></span>
      <h1 class="company__name">Halvern Inspection Services, LLC</h1>
    </div>
    <div class="contact-band">
      <span class="contact-band__name">Dale Halvern</span>
      <span class="contact-band__sep">|</span>
      <span class="contact-band__phone">(989) 514-2730</span>
      <span class="contact-band__sep">|</span>
      <span class="contact-band__email">halv7dw@mailbreeze.net</span>
    </div>
  </section>

  <section class="card card--back" aria-label="Business card back">
    <div class="credentials">
      <ul class="credentials__group">
        <li>NWCA Certified Welding Inspector</li>
        <li>NWCA Certified Radiographic Interpreter</li>
        <li>NWCA Certified Welding Educator</li>
      </ul>
      <ul class="credentials__group">
        <li>Level II - Ultrasonic Testing</li>
        <li class="credentials__method">Magnetic Particle Testing</li>
        <li class="credentials__method">Liquid Penetrant Testing</li>
      </ul>
    </div>
  </section>
</main>
</body>
</html>
```